Bright Path Attorneys Billboard Design for Personal Injury Law Firm

Need a billboard design that we can use for different versions. 1400px X 400px jpeg or png
I have attached the logo and the attorney for the billboard. Attorney Marla Benning
Here is a link to our current website brightpathlegalgroup.example

HEADLINE: HIT BY A TRUCK?
SUBHEAD: NO FEE. BIG FIGHT.
877-GRANTLY

HEADLINE: ACCIDENT?
SUBHEAD: NO FEE, UNLESS WE WIN!
877-GRANTLY

HEADLINE: BIG TRUCK. BIG CASE.
SUBHEAD: YOU PAY $0 UPFRONT
877-GRANTLY

Target Market(s)

People in Car Accident

Industry/Entity Type

Personal Injury Attorneys

```html
<!DOCTYPE html>
<html lang="en">
<head>
<meta charset="utf-8">
<title>Bright Path Attorneys – Billboard Set</title>
<link rel="stylesheet" href="https://fonts.googleapis.com/css2?family=Poppins:wght@800;900&family=Oswald:wght@500;600;700&family=Fredoka:wght@700&family=Archivo+Black&family=Anton&family=Montserrat:wght@600&display=swap">
<style>
  :root{
    --navy:#0a101d;
    --footer:#0e1a33;
    --yellow:#fec20e;
    --green:#2fce3b;
    --lime:#9af01c;
    --white:#ffffff;
    --light:#e6e6e6;
    --sky:#1ec8f5;
    --grey:#b9bcc2;
  }
  *{margin:0;padding:0;box-sizing:border-box}
  html,body{width:1200px;height:1155px;overflow:hidden;background:#fff}
  .board{position:absolute;left:0;width:1200px;height:343px;background:var(--navy);overflow:hidden}
  .board--truck{top:0}
  .board--accident{top:400px}
  .board--case{top:812px}
  .attorney-photo{position:absolute;left:0;top:38px;width:242px;height:245px;
    background:radial-gradient(ellipse at 50% 30%,#d9b894 0 22%,transparent 23%),
               linear-gradient(180deg,#b38a5e 0%,#8d6a49 40%,#1a2133 60%,#141b2c 100%);
    border-radius:110px 110px 0 0}
  .scene-photo{position:absolute;top:0;right:0;height:283px}
  .board--truck .scene-photo{width:440px;background:linear-gradient(90deg,var(--navy) 0%,#6b6a74 25%,#b8a79e 55%,#7b7f86 80%,#3f4650 100%)}
  .board--accident .scene-photo{width:410px;background:linear-gradient(90deg,var(--navy) 0%,#2d3442 25%,#4c5566 55%,#8b8f92 85%,#a9aaa8 100%)}
  .board--case .scene-photo{width:470px;background:linear-gradient(90deg,var(--navy) 0%,#3a2630 22%,#8c2a2c 50%,#6c6e72 75%,#2b3340 100%)}
  .copy{position:absolute;left:0;right:0;top:0;height:283px}
  .headline,.subhead,.phone-box,.upfront,.big-case{position:absolute;white-space:nowrap}
  .headline--truck{left:196px;top:36px;font-family:"Poppins",sans-serif;font-weight:900;font-size:84px;line-height:1;letter-spacing:-1px;
    background:linear-gradient(180deg,var(--sky) 0%,#7fe1ff 55%,var(--white) 100%);-webkit-background-clip:text;background-clip:text;color:transparent}
  .subhead--truck{left:321px;top:126px;font-family:"Oswald",sans-serif;font-weight:700;font-size:50px;line-height:1;color:var(--white)}
  .headline--accident{left:287px;top:42px;font-family:"Fredoka",sans-serif;font-weight:700;font-size:88px;line-height:1;color:var(--yellow);letter-spacing:1px}
  .subhead--accident{left:221px;top:126px;font-family:"Oswald",sans-serif;font-weight:700;font-size:58px;line-height:1;color:var(--light)}
  .big-case{left:320px;top:36px;font-family:"Oswald",sans-serif;font-weight:700;font-size:62px;line-height:1;color:var(--lime);letter-spacing:-1px}
  .you-pay{position:absolute;left:274px;top:102px;width:134px;height:97px;background:var(--yellow);border-radius:10px;
    font-family:"Archivo Black",sans-serif;font-size:40px;line-height:40px;color:#0c1530;text-align:center;padding-top:8px}
  .upfront{left:430px;top:108px;font-family:"Anton",sans-serif;font-size:86px;line-height:1;color:var(--white)}
  .upfront .amount{color:var(--lime)}
  .phone-box{border:1px solid var(--green);font-family:"Oswald",sans-serif;font-weight:600;line-height:1;text-align:center;color:var(--yellow)}
  .phone-box .area{color:var(--green)}
  .board--truck .phone-box{left:287px;top:187px;width:521px;height:70px;font-size:60px;padding-top:2px}
  .board--accident .phone-box,.board--case .phone-box{left:301px;width:475px;height:66px;font-size:57px;padding-top:2px}
  .board--accident .phone-box{top:202px}
  .board--case .phone-box{top:205px}
  .footer{position:absolute;left:0;bottom:0;width:1200px;height:60px;background:var(--footer);display:flex;align-items:center;
    font-family:"Oswald",sans-serif;color:var(--white)}
  .footer .site{width:290px;padding-left:40px;font-size:20px;font-weight:500;color:var(--yellow)}
  .footer .contact{display:flex;align-items:center;gap:5px;font-size:13px;font-weight:500;padding:0 8px;height:28px}
  .footer .contact + .contact{border-left:2px solid var(--grey)}
  .footer svg{width:11px;height:11px;fill:var(--lime)}
  .brand{margin-left:auto;margin-right:30px;display:flex;align-items:center;gap:8px;font-family:"Montserrat",sans-serif;font-weight:600;font-size:17px;color:var(--white)}
  .brand-mark{width:14px;height:14px;background:var(--lime)}
</style>
</head>
<body>

<section class="board board--truck">
  <div class="scene-photo" role="img" aria-label="Semi truck trailer on a highway at dusk"></div>
  <div class="attorney-photo" role="img" aria-label="Portrait of attorney Marla Benning, arms crossed, navy blazer"></div>
  <div class="copy">
    <h1 class="headline headline--truck">HIT BY A TRUCK?</h1>
    <p class="subhead subhead--truck">NO FEE. BIG FIGHT</p>
    <p class="phone-box"><span class="area">877</span>-GRANTLY</p>
  </div>
  <footer class="footer">
    <span class="site">brightpathlegalgroup.example</span>
    <span class="contact"><svg viewBox="0 0 24 24"><path d="M6.6 10.8a15 15 0 0 0 6.6 6.6l2.2-2.2c.3-.3.7-.4 1-.2 1.1.4 2.3.6 3.6.6.6 0 1 .4 1 1V20c0 .6-.4 1-1 1A17 17 0 0 1 3 4c0-.6.4-1 1-1h3.5c.6 0 1 .4 1 1 0 1.3.2 2.5.6 3.6.1.3 0 .7-.2 1z"/></svg>8665550142</span>
    <span class="contact"><svg viewBox="0 0 24 24"><path d="M2 5h20v14H2zM3 6l9 7 9-7"/></svg>hello@brightpathlegalgroup.example</span>
    <span class="contact"><svg viewBox="0 0 24 24"><path d="M12 2a7 7 0 0 0-7 7c0 5 7 13 7 13s7-8 7-13a7 7 0 0 0-7-7zm0 9.5A2.5 2.5 0 1 1 12 6a2.5 2.5 0 0 1 0 5.5z"/></svg>125 harbor point dr, suite 410, marietta, ga 30060</span>
    <span class="brand"><span class="brand-mark"></span>Bright Path Attorneys</span>
  </footer>
</section>

<section class="board board--accident">
  <div class="scene-photo" role="img" aria-label="Damaged dark sedan with crushed front after a collision"></div>
  <div class="attorney-photo" role="img" aria-label="Portrait of attorney Marla Benning, arms crossed, navy blazer"></div>
  <div class="copy">
    <h1 class="headline headline--accident">ACCIDENT?</h1>
    <p class="subhead subhead--accident">NO FEE, UNLESS WE WIN!</p>
    <p class="phone-box"><span class="area">877</span>-GRANTLY</p>
  </div>
  <footer class="footer">
    <span class="site">brightpathlegalgroup.example</span>
    <span class="contact"><svg viewBox="0 0 24 24"><path d="M6.6 10.8a15 15 0 0 0 6.6 6.6l2.2-2.2c.3-.3.7-.4 1-.2 1.1.4 2.3.6 3.6.6.6 0 1 .4 1 1V20c0 .6-.4 1-1 1A17 17 0 0 1 3 4c0-.6.4-1 1-1h3.5c.6 0 1 .4 1 1 0 1.3.2 2.5.6 3.6.1.3 0 .7-.2 1z"/></svg>8665550142</span>
    <span class="contact"><svg viewBox="0 0 24 24"><path d="M2 5h20v14H2zM3 6l9 7 9-7"/></svg>hello@brightpathlegalgroup.example</span>
    <span class="contact"><svg viewBox="0 0 24 24"><path d="M12 2a7 7 0 0 0-7 7c0 5 7 13 7 13s7-8 7-13a7 7 0 0 0-7-7zm0 9.5A2.5 2.5 0 1 1 12 6a2.5 2.5 0 0 1 0 5.5z"/></svg>125 harbor point dr, suite 410, marietta, ga 30060</span>
    <span class="brand"><span class="brand-mark"></span>Bright Path Attorneys</span>
  </footer>
</section>

<section class="board board--case">
  <div class="scene-photo" role="img" aria-label="Red semi truck cab with chrome grille"></div>
  <div class="attorney-photo" role="img" aria-label="Portrait of attorney Marla Benning, arms crossed, navy blazer"></div>
  <div class="copy">
    <h1 class="big-case">BIG TRUCK. BIG CASE.</h1>
    <div class="you-pay">YOU<br>PAY</div>
    <p class="upfront"><span class="amount">$0</span> UPFRONT</p>
    <p class="phone-box"><span class="area">877</span>-GRANTLY</p>
  </div>
  <footer class="footer">
    <span class="site">brightpathlegalgroup.example</span>
    <span class="contact"><svg viewBox="0 0 24 24"><path d="M6.6 10.8a15 15 0 0 0 6.6 6.6l2.2-2.2c.3-.3.7-.4 1-.2 1.1.4 2.3.6 3.6.6.6 0 1 .4 1 1V20c0 .6-.4 1-1 1A17 17 0 0 1 3 4c0-.6.4-1 1-1h3.5c.6 0 1 .4 1 1 0 1.3.2 2.5.6 3.6.1.3 0 .7-.2 1z"/></svg>8665550142</span>
    <span class="contact"><svg viewBox="0 0 24 24"><path d="M2 5h20v14H2zM3 6l9 7 9-7"/></svg>hello@brightpathlegalgroup.example</span>
    <span class="contact"><svg viewBox="0 0 24 24"><path d="M12 2a7 7 0 0 0-7 7c0 5 7 13 7 13s7-8 7-13a7 7 0 0 0-7-7zm0 9.5A2.5 2.5 0 1 1 12 6a2.5 2.5 0 0 1 0 5.5z"/></svg>125 harbor point dr, suite 410, marietta, ga 30060</span>
    <span class="brand"><span class="brand-mark"></span>Bright Path Attorneys</span>
  </footer>
</section>

</body>
</html>
```